Brimovex business card

Based on company logo and website given , to design a business card temple. Slogan "Your furry friends deserves the best"
Color style please refer to our website

```html
<!DOCTYPE html>
<html lang="en">
<head>
<meta charset="UTF-8">
<title>Brimovex Business Card</title>
<link rel="stylesheet" href="https://fonts.googleapis.com/css2?family=Oswald:wght@400;500&display=swap">
<style>
  :root {
    --page-bg: #ffffff;
    --forest: #0b2d2d;
    --mist: #eef7f8;
    --gold: #f5d000;
    --white: #ffffff;
  }
  * { margin: 0; padding: 0; box-sizing: border-box; }
  html, body {
    width: 1200px;
    height: 1200px;
    overflow: hidden;
    background: var(--page-bg);
    font-family: "Oswald", sans-serif;
  }
  .canvas {
    position: relative;
    width: 1200px;
    height: 1200px;
  }
  .card {
    position: absolute;
    left: 260px;
    width: 679px;
    height: 416px;
    border-radius: 20px;
    text-align: center;
  }
  .card-front {
    top: 159px;
    background: var(--forest);
  }
  .card-back {
    top: 637px;
    background: var(--mist);
    color: var(--forest);
  }
  .brand-name {
    position: absolute;
    left: 0;
    right: 0;
    top: 142px;
    font-size: 66px;
    font-weight: 500;
    line-height: 1;
    color: var(--gold);
    letter-spacing: 1px;
  }
  .tagline {
    position: absolute;
    left: 0;
    right: 0;
    top: 236px;
    font-size: 20px;
    font-weight: 400;
    line-height: 1;
    color: var(--white);
  }
  .person-name {
    position: absolute;
    left: 0;
    right: 0;
    top: 70px;
    font-size: 38px;
    font-weight: 500;
    line-height: 1;
  }
  .person-role {
    position: absolute;
    left: 0;
    right: 0;
    top: 125px;
    font-size: 20px;
    font-weight: 400;
    line-height: 1;
  }
  .contact-list {
    position: absolute;
    left: 0;
    right: 0;
    top: 184px;
    list-style: none;
    font-size: 21px;
    line-height: 32px;
    font-weight: 400;
  }
  .website-pill {
    position: absolute;
    left: 213px;
    top: 290px;
    width: 252px;
    height: 28px;
    border-radius: 14px;
    background: var(--forest);
    color: var(--white);
    font-size: 20px;
    line-height: 28px;
  }
</style>
</head>
<body>
  <main class="canvas">
    <section class="card card-front">
      <div class="brand-name">Brimovex</div>
      <p class="tagline">Your furry friends deserves the best</p>
    </section>

    <section class="card card-back">
      <h1 class="person-name">Marcus Hale</h1>
      <p class="person-role">CEO</p>
      <ul class="contact-list">
        <li class="contact-address">12/48 Harlow Street Kelmsford Vic 3187</li>
        <li class="contact-phone">+61 3 9046 2815</li>
        <li class="contact-email">info@brimovex.com.au</li>
      </ul>
      <div class="website-pill">www.brimovex.com.au</div>
    </section>
  </main>
</body>
</html>
```